Navelo Partnering Business Card

Hello everyone. We need a business card design that would match our logo and the theme we're trying to have for Navelo that you can find on our website and/or Corvapage page

```html
<!DOCTYPE html>
<html lang="en">
<head>
<meta charset="utf-8">
<title>Navelo Partnering Business Card</title>
<link rel="stylesheet" href="https://fonts.googleapis.com/css2?family=Questrial&display=swap">
<style>
  :root {
    --teal: #00a098;
    --navy: #022b5b;
    --paper: #eff0f2;
    --white: #ffffff;
    --backdrop: #e4e4e2;
  }
  * { box-sizing: border-box; margin: 0; padding: 0; }
  html, body { width: 1200px; height: 1200px; overflow: hidden; }
  body {
    background: var(--backdrop);
    font-family: "Questrial", "Century Gothic", sans-serif;
    position: relative;
  }
  .card {
    position: absolute;
    left: 250px;
    width: 700px;
    height: 400px;
    overflow: hidden;
    box-shadow: 0 6px 18px rgba(0,0,0,0.12);
  }
  /* Front */
  .card-front { top: 150px; background: var(--teal); color: var(--white); }
  .card-front .wordmark {
    position: absolute;
    left: 60px; top: 170px;
    width: 230px;
    text-align: center;
    display: flex; align-items: center; justify-content: center; gap: 10px;
  }
  .wordmark-name { font-size: 40px; letter-spacing: 0.5px; line-height: 1; }
  .wordmark-dot { width: 14px; height: 14px; border-radius: 50%; background: currentColor; }
  .card-front .divider {
    position: absolute; left: 330px; top: 90px;
    width: 1px; height: 220px; background: rgba(255,255,255,0.6);
  }
  .card-front .company {
    position: absolute; left: 370px; top: 96px;
    font-size: 17px; letter-spacing: 1px;
  }
  /* Back */
  .card-back { top: 650px; background: var(--paper); }
  .card-back .brand-side {
    position: absolute; left: 0; top: 0; width: 320px; height: 100%;
    display: flex; align-items: center; justify-content: center;
    color: var(--navy);
  }
  .card-back .brand-side .wordmark { display: flex; align-items: center; gap: 12px; }
  .card-back .brand-side .wordmark-name { font-size: 52px; }
  .card-back .brand-side .wordmark-dot { width: 18px; height: 18px; }
  .card-back .contact-side {
    position: absolute; left: 320px; top: 0; right: 0; height: 100%;
    background: var(--navy);
    padding: 110px 0 0 52px;
  }
  .contact-list { list-style: none; }
  .contact-item {
    display: flex; align-items: center; gap: 18px;
    margin-bottom: 22px;
    color: var(--teal); font-size: 16px; line-height: 1.35; letter-spacing: 0.5px;
  }
  .contact-icon {
    flex: 0 0 42px; width: 42px; height: 42px;
    background: var(--teal);
    display: flex; align-items: center; justify-content: center;
  }
  .contact-icon svg { width: 22px; height: 22px; }
</style>
</head>
<body>
  <section class="card card-front" aria-label="Card front">
    <div class="wordmark">
      <span class="wordmark-name">Navelo</span>
      <span class="wordmark-dot"></span>
    </div>
    <div class="divider"></div>
    <p class="company">Navelo Partnering Ltd.</p>
  </section>

  <section class="card card-back" aria-label="Card back">
    <div class="brand-side">
      <div class="wordmark">
        <span class="wordmark-name">Navelo</span>
        <span class="wordmark-dot"></span>
      </div>
    </div>
    <div class="contact-side">
      <ul class="contact-list">
        <li class="contact-item">
          <span class="contact-icon">
            <svg viewBox="0 0 24 24" aria-hidden="true"><path fill="#022b5b" d="M6.6 10.8a15.1 15.1 0 0 0 6.6 6.6l2.2-2.2a1 1 0 0 1 1-.25 11.4 11.4 0 0 0 3.6.57 1 1 0 0 1 1 1V20a1 1 0 0 1-1 1A17 17 0 0 1 3 4a1 1 0 0 1 1-1h3.5a1 1 0 0 1 1 1c0 1.25.2 2.45.57 3.57a1 1 0 0 1-.25 1z"/></svg>
          </span>
          <span>+44 2079460321</span>
        </li>
        <li class="contact-item">
          <span class="contact-icon">
            <svg viewBox="0 0 24 24" aria-hidden="true"><path fill="#022b5b" d="M12 2a7 7 0 0 0-7 7c0 5.2 7 13 7 13s7-7.8 7-13a7 7 0 0 0-7-7zm0 9.5A2.5 2.5 0 1 1 12 6.5a2.5 2.5 0 0 1 0 5z"/></svg>
          </span>
          <span>The Linden Court Place,<br>Crawley, RH10 9QX, UK</span>
        </li>
        <li class="contact-item">
          <span class="contact-icon">
            <svg viewBox="0 0 24 24" aria-hidden="true"><g fill="none" stroke="#022b5b" stroke-width="1.6"><circle cx="12" cy="12" r="9"/><ellipse cx="12" cy="12" rx="4" ry="9"/><path d="M3 12h18M4.5 7.5h15M4.5 16.5h15"/></g></svg>
          </span>
          <span>www.navelopartnering.com</span>
        </li>
      </ul>
    </div>
  </section>
</body>
</html>
```